Company Values Graphic

We are looking for a design of our company values that can be used in a variety of places including our website, mousepads, office posters, business cards, etc.

Notes:
- We'd rather have icons/art than photographs on the poster.... so more like an infographic
- The core value group headings are not required, but can be included if you think grouping the values works for your design
- We have a logo for our software product but that logo is not required
- We don't need/want clever images to accompany each value, but some images are fine
- BrightNest logo attached
- BrightNest colors are attached
- BrightNest logo is Nunito Sans ExtraBold 800
- BrightNest website uses Roboto

Our Values - Who we will work with (and who we will not)
The right set of values are essential to building and maintaining a culture that we all wake up eager to be a part of each day. They are foundational to all hiring and firing decisions. They attract the right people and repel the wrong ones.

BE HELPFUL
Make every person and place better because you are there.
Deliver wow with every interaction.

BE HUMBLE
Listen with every muscle.
Passionately help others first.
Seek first to understand.

BE HONEST
Earn trust every day.
Be open and direct.
Treat everyone with fairness and respect.

BE HUMAN
Celebrate passion and action.
Create an environment where people are authentic.
Hire great people and expect a lot from them

BE COURAGEOUS
Dare mighty things.
Make and honor commitments.
All great things start with a small act of courage applied at the right moment.

```html
<!DOCTYPE html>
<html lang="en">
<head>
<meta charset="utf-8">
<title>BrightNest — Our Values</title>
<link rel="stylesheet" href="https://fonts.googleapis.com/css2?family=League+Gothic&family=Roboto:wght@400;700;800&display=swap">
<style>
  :root {
    --paper: #f2f2f2;
    --ink: #000000;
    --icon-tone: #151515;
    --white: #ffffff;
    --orange: #ff9900;
    --ember: #ff5a00;
    --red: #ff0000;
  }
  * { margin: 0; padding: 0; box-sizing: border-box; }
  html, body { width: 902px; height: 1200px; overflow: hidden; background: var(--paper); }
  .poster { position: relative; width: 902px; height: 1200px; background: var(--paper); font-family: "Roboto", sans-serif; }

  .spine { position: absolute; left: 338px; top: 0; width: 229px; height: 1200px; background: var(--ink); }
  .brand { position: absolute; left: 338px; width: 229px; top: 140px; text-align: center;
           font-family: "Roboto", sans-serif; font-weight: 800; font-size: 36px; color: var(--orange); }
  .title { position: absolute; left: 338px; width: 229px; text-align: center; color: var(--white);
           font-family: "League Gothic", sans-serif; line-height: 1; }
  .title-our { top: 284px; font-size: 162px; }
  .title-values { top: 426px; font-size: 90px; }
  .subtitle { position: absolute; left: 338px; width: 229px; top: 524px; text-align: center;
              color: var(--white); font-weight: 700; font-size: 28px; line-height: 33.6px; }
  .intro { position: absolute; left: 338px; width: 229px; top: 690px; text-align: center;
           color: var(--white); font-weight: 400; font-size: 21.5px; line-height: 26.6px; }

  .dot { position: absolute; width: 15px; height: 15px; border-radius: 50%; transform: translate(-50%, -50%); }
  .dot-orange { background: var(--orange); }
  .dot-ember { background: var(--ember); }
  .dot-red { background: var(--red); }

  .pictogram { position: absolute; background: var(--icon-tone); border-radius: 14px 14px 0 0; }

  .value-card { position: absolute; }
  .value-card svg { position: absolute; left: 0; top: 0; }
  .value-card.is-right svg { transform: scaleX(-1); }
  .value-title { position: absolute; top: 8px; left: 48px; color: var(--white);
                 font-family: "League Gothic", sans-serif; font-size: 40px; line-height: 40px; }
  .value-card.is-right .value-title { left: 66px; }
  .value-points { position: absolute; top: 73px; left: 23px; right: 40px; list-style: none;
                  color: var(--white); font-weight: 700; font-size: 14.5px; line-height: 15px; }
  .value-card.is-right .value-points { left: 43px; right: 14px; }
  .value-points li { position: relative; padding-left: 7px; margin-bottom: 7px; }
  .value-points li::before { content: "•"; position: absolute; left: -1px; font-size: 10px; }
  .fill-orange { fill: var(--orange); }
  .fill-ember { fill: var(--ember); }
  .fill-red { fill: var(--red); }
  .fill-ink { fill: var(--ink); }
</style>
</head>
<body>
<main class="poster">
  <div class="spine"></div>
  <div class="brand">BrightNest</div>
  <h1 class="title title-our">OUR</h1>
  <div class="title title-values">VALUES</div>
  <p class="subtitle">(Who we will<br>work with<br>and who we<br>will not)</p>
  <p class="intro">The right set of<br>values are<br>essential to<br>building and<br>maintaining a<br>culture that we<br>all wake up<br>eager to be a<br>part of each day.<br>They are<br>foundational to<br>all hiring and<br>firing decisions.<br>They attract the<br>right people and<br>repel the wrong<br>ones.</p>

  <!-- Be Helpful -->
  <div class="pictogram" role="img" aria-label="Pictogram of one person helping another climb up a step" style="left:33px;top:35px;width:157px;height:152px;"></div>
  <section class="value-card" style="left:31px;top:186px;width:281px;height:184px;">
    <svg width="281" height="184" viewBox="0 0 281 184">
      <path class="fill-ink" d="M0,0 H233 A27,27 0 0 1 260,27 V90 H0 Z"/>
      <path class="fill-orange" d="M0,54 H233 A27,27 0 0 1 260,81 V162 L280,184 H33 A33,33 0 0 1 0,151 Z"/>
    </svg>
    <h2 class="value-title">BE HELPFUL</h2>
    <ul class="value-points">
      <li>Make every person and place better because you are there.</li>
      <li>Deliver wow with every interaction.</li>
    </ul>
  </section>
  <span class="dot dot-orange" style="left:338px;top:369px;"></span>

  <!-- Be Honest -->
  <div class="pictogram" role="img" aria-label="Pictogram of two people talking with a speech bubble" style="left:34px;top:426px;width:156px;height:128px;"></div>
  <section class="value-card" style="left:31px;top:553px;width:281px;height:183px;">
    <svg width="281" height="183" viewBox="0 0 281 183">
      <path class="fill-ink" d="M0,0 H233 A27,27 0 0 1 260,27 V90 H0 Z"/>
      <path class="fill-red" d="M0,54 H233 A27,27 0 0 1 260,81 V161 L280,183 H33 A33,33 0 0 1 0,150 Z"/>
    </svg>
    <h2 class="value-title">BE HONEST</h2>
    <ul class="value-points">
      <li>Earn trust every day.</li>
      <li>Be open and direct.</li>
      <li>Treat everyone with fairness and respect.</li>
    </ul>
  </section>
  <span class="dot dot-red" style="left:338px;top:734px;"></span>

  <!-- Be Courageous -->
  <div class="pictogram" role="img" aria-label="Pictogram of a person leaping between mountain peaks toward a flag" style="left:31px;top:785px;width:237px;height:160px;"></div>
  <section class="value-card" style="left:31px;top:944px;width:281px;height:206px;">
    <svg width="281" height="206" viewBox="0 0 281 206">
      <path class="fill-ink" d="M0,0 H233 A27,27 0 0 1 260,27 V90 H0 Z"/>
      <path class="fill-red" d="M0,54 H233 A27,27 0 0 1 260,81 V184 L280,206 H33 A33,33 0 0 1 0,173 Z"/>
    </svg>
    <h2 class="value-title">BE COURAGEOUS</h2>
    <ul class="value-points">
      <li>Dare mighty things.</li>
      <li>Make and honor commitments.</li>
      <li>All great things start with a small act of courage applied at the right moment.</li>
    </ul>
  </section>
  <span class="dot dot-red" style="left:338px;top:1150px;"></span>

  <!-- Be Humble -->
  <div class="pictogram" role="img" aria-label="Pictogram of one person listening to another who raises a finger" style="left:684px;top:262px;width:188px;height:109px;"></div>
  <section class="value-card is-right" style="left:591px;top:370px;width:281px;height:183px;">
    <svg width="281" height="183" viewBox="0 0 281 183">
      <path class="fill-ink" d="M0,0 H233 A27,27 0 0 1 260,27 V90 H0 Z"/>
      <path class="fill-ember" d="M0,54 H233 A27,27 0 0 1 260,81 V161 L280,183 H33 A33,33 0 0 1 0,150 Z"/>
    </svg>
    <h2 class="value-title">BE HUMBLE</h2>
    <ul class="value-points">
      <li>Listen with every muscle.</li>
      <li>Passionately help others first.</li>
      <li>Seek first to understand.</li>
    </ul>
  </section>
  <span class="dot dot-ember" style="left:567px;top:553px;"></span>

  <!-- Be Human -->
  <div class="pictogram" role="img" aria-label="Pictogram of a team gathered around a meeting table" style="left:696px;top:583px;width:176px;height:154px;"></div>
  <section class="value-card is-right" style="left:591px;top:736px;width:281px;height:206px;">
    <svg width="281" height="206" viewBox="0 0 281 206">
      <path class="fill-ink" d="M0,0 H233 A27,27 0 0 1 260,27 V90 H0 Z"/>
      <path class="fill-orange" d="M0,54 H233 A27,27 0 0 1 260,81 V184 L280,206 H33 A33,33 0 0 1 0,173 Z"/>
    </svg>
    <h2 class="value-title">BE HUMAN</h2>
    <ul class="value-points">
      <li>Celebrate passion and action.</li>
      <li>Create an environment where people are authentic.</li>
      <li>Hire great people and expect a lot from them</li>
    </ul>
  </section>
  <span class="dot dot-orange" style="left:567px;top:942px;"></span>
</main>
</body>
</html>
```